WE HAND MAKE AND DECORATE BEAUTIFUL CREATIVE GINGER BREAD HOUSES FOR CHRISTMAS AND CUPCAKES FOR SPECIAL OCCASIONS

Contact Information for Business Card

PIPPIN AND MARLOW DESIGNS
ROSA 0467 213 905
MAVIS 0438104629

```html
<!DOCTYPE html>
<html lang="en">
<head>
<meta charset="utf-8">
<title>Pippin and Marlow Designs – Business Card</title>
<link rel="stylesheet" href="https://fonts.googleapis.com/css2?family=Lato:wght@400;700&display=swap">
<style>
  :root {
    --backdrop: #6e6e6e;
    --card-light: #d6d0c8;
    --card-mid: #a08670;
    --card-dark: #6b4a2f;
    --photo-wall: #c9cdd1;
    --photo-roof: #6f4f3b;
    --photo-gingerbread: #8e6c55;
    --photo-icing: #ebe7e2;
    --photo-candy: #b4606a;
    --text-light: #ffffff;
  }
  html, body {
    margin: 0;
    width: 1200px;
    height: 900px;
    overflow: hidden;
    background: var(--backdrop);
    font-family: "Lato", sans-serif;
  }
  .business-card {
    position: absolute;
    left: 100px;
    top: 160px;
    width: 1000px;
    height: 580px;
    border-radius: 34px;
    overflow: hidden;
    background:
      radial-gradient(ellipse 45% 60% at 55% 35%, var(--card-light) 0%, transparent 70%),
      linear-gradient(110deg, var(--card-light) 20%, var(--card-mid) 60%, var(--card-dark) 100%);
  }
  .product-photo {
    position: absolute;
    left: 0;
    top: 0;
    width: 480px;
    height: 100%;
    background:
      linear-gradient(180deg, transparent 78%, var(--photo-icing) 86%, var(--photo-icing) 100%),
      radial-gradient(ellipse 18% 10% at 50% 38%, var(--photo-candy) 0%, transparent 100%),
      linear-gradient(180deg, var(--photo-roof) 0%, var(--photo-gingerbread) 40%, var(--photo-gingerbread) 100%) 50% 12% / 76% 76% no-repeat,
      linear-gradient(180deg, var(--photo-wall) 0%, #dcdfe1 100%);
    -webkit-mask-image: linear-gradient(90deg, #000 82%, transparent 100%);
    mask-image: linear-gradient(90deg, #000 82%, transparent 100%);
  }
  .business-name {
    position: absolute;
    right: 40px;
    top: 56px;
    margin: 0;
    text-align: right;
    color: var(--text-light);
    font-weight: 700;
    font-size: 34px;
    line-height: 1.3;
    letter-spacing: 0.3px;
  }
  .contact-list {
    position: absolute;
    right: 40px;
    top: 360px;
    margin: 0;
    padding: 0;
    list-style: none;
    text-align: right;
    color: var(--text-light);
  }
  .contact {
    margin: 0 0 18px;
  }
  .contact-name {
    display: block;
    font-weight: 400;
    font-size: 34px;
    letter-spacing: 0.8px;
    line-height: 1.2;
  }
  .contact-phone {
    display: block;
    font-weight: 700;
    font-size: 28px;
    letter-spacing: 0.4px;
    line-height: 1.3;
  }
</style>
</head>
<body>
  <article class="business-card">
    <div class="product-photo" role="img" aria-label="Photo of a handmade decorated gingerbread house with candy canes and white icing"></div>
    <h1 class="business-name">PIPPIN AND MARLOW<br>DESIGNS</h1>
    <ul class="contact-list">
      <li class="contact">
        <span class="contact-name">ROSA</span>
        <span class="contact-phone">0467 213 905</span>
      </li>
      <li class="contact">
        <span class="contact-name">MAVIS</span>
        <span class="contact-phone">0438 104 629</span>
      </li>
    </ul>
  </article>
</body>
</html>
```